Destination Wedding Photographer

I am a Wedding photographer based in San Juan, Puerto Rico. The banner will be shown in the United States to brides that plan to have their wedding in Puerto Rico.

I want to highlight the following words/phrases
Puerto Rico
Destination Wedding
Photographer
(in that order)

feel free to get creative adding your own inspired text.

My web site: www.benitolavarro.com

Target Market(s)

Brides in the united states looking for a photographer for their wedding in Puerto Rico

Industry/Entity Type

Wedding

Requirements
Must have
• + Your ad must be a .gif, .png or .jpg smaller than 40kb in filesize
+ include the following sizes: 300x250, 728x90, 160x600, 468x60, or 120x600
+ Your ad must include the advertiser's brand
+ Your ad must have a border
Should not have
• + Your ad cannot imitate computer effects like scrolling or mousing over
+ No animations longer than 30 seconds
+ No strobe or flashing effects allowed
+ Your ad and campaign must not feature or promote alcohol, anabolic steroids, drugs, financial products, gambling, adult content, or weight loss products

```html
<!DOCTYPE html>
<html lang="en">
<head>
<meta charset="utf-8">
<title>Benito Lavarro Photography – Destination Wedding Photographer</title>
<link rel="stylesheet" href="https://fonts.googleapis.com/css2?family=Quicksand:wght@300;400;500&display=swap">
<style>
  :root {
    --frame: #ffffff;
    --sky-top: #2f86cf;
    --sky-mid: #5aa6e2;
    --sky-low: #8fc3ec;
    --grass: #4f8a2a;
    --grass-dark: #3b6d1c;
    --couple-light: #d9dcd6;
    --couple-dark: #8a8478;
    --ink: #ffffff;
  }
  html, body {
    margin: 0;
    padding: 0;
    width: 1200px;
    height: 320px;
    overflow: hidden;
    background: var(--frame);
  }
  .banner {
    position: relative;
    width: 1200px;
    height: 320px;
    background: var(--frame);
  }
  .banner__scene {
    position: absolute;
    left: 24px;
    top: 24px;
    width: 1152px;
    height: 276px;
    background: linear-gradient(180deg,
      var(--sky-top) 0%,
      var(--sky-mid) 45%,
      var(--sky-low) 88%,
      var(--grass) 91%,
      var(--grass-dark) 100%);
  }
  .banner__couple {
    position: absolute;
    left: 236px;
    top: 52px;
    width: 186px;
    height: 228px;
    border-radius: 60px 60px 12px 12px;
    background: linear-gradient(180deg, var(--couple-light) 0%, var(--couple-dark) 100%);
    opacity: 0.9;
  }
  .brand {
    position: absolute;
    left: 800px;
    top: 74px;
    width: 370px;
    text-align: center;
    color: var(--ink);
    font-family: "Quicksand", sans-serif;
    font-weight: 300;
  }
  .brand__name {
    margin: 0;
    font-size: 50px;
    line-height: 1;
    letter-spacing: 1px;
  }
  .brand__label {
    margin: 6px 0 0;
    font-size: 13px;
    letter-spacing: 7px;
    text-transform: uppercase;
  }
  .tagline {
    margin: 24px 0 0;
    font-size: 16px;
    letter-spacing: 2.5px;
    line-height: 1.3;
  }
  .tagline__place {
    display: block;
    margin-top: 4px;
    font-size: 22px;
    font-weight: 500;
    letter-spacing: 3px;
  }
</style>
</head>
<body>
  <div class="banner">
    <div class="banner__scene" role="img" aria-label="Clear blue sky over a grassy hilltop"></div>
    <div class="banner__couple" role="img" aria-label="Photo of an engaged couple dancing in a dip on the hilltop"></div>
    <div class="brand">
      <p class="brand__name">Benito Lavarro</p>
      <p class="brand__label">Photography</p>
      <p class="tagline">Destination Wedding Photographer<span class="tagline__place">~Puerto Rico~</span></p>
    </div>
  </div>
</body>
</html>
```